Boot Camp Flyer

Outdoor Boot Camp
SAMPLE DESIGNS I LIKE UPLOADED.
Similar to this or be creative !
I need A5 and DL flyer promoting our Boot Camp program, similar to the sample design but include our details. Pink blue green black white yellow and purple colours ok

PRICE: $100
WHEN: Thursdays & Saturdays
Thursday 6pm
Saturday 9am

WHERE: Brindmoor Glen

Get results all year round! 5 week boot camp only $100
Join in any time! Register your place now!

Stride Forge Boot Camp
Register now at lumatrekgym@mailvera.com or www.socialpage-example.com/lumatrekgymnz
Female only. Registration essential. ALL fitness levels welcome.

Conditions
Valid from Mar 22, 2018
Expires 26th Apr, 2018
Register online. Subject to availability. Valid for new clients only. Valid for unlimited sessions per week. Boot Camps run in 5 week blocks. Non-transferable. No refunds unless required by law. No cashback. Not to be used with any other offer.

Could maybe write 5 week stride forge challenge

Target Market(s)

Female 20s-40s

Industry/Entity Type

Fitness

Colors

Requirements
Must have
• Colour
• Easy to read font
• Picture of females (target market) exercising
Nice to have
• Terms and conditions in small print down bottom.
Should not have
• Too much text

```html
<!DOCTYPE html>
<html lang="en">
<head>
<meta charset="utf-8">
<title>Boot Camp Flyer – Lumatrek Gym</title>
<link rel="stylesheet" href="https://fonts.googleapis.com/css2?family=Roboto:wght@400;700;900&family=Teko:wght@400;500&family=Open+Sans:wght@400&display=swap">
<style>
  :root {
    --stage: #2b2d30;
    --ink: #0b0b0d;
    --paper: #ffffff;
    --yellow: #f6ea4c;
    --pink: #e5168a;
    --purple: #8a3fd1;
    --blue: #1e9bdc;
    --sky: #37b6f0;
    --rule: #7a7a7a;
  }
  * { box-sizing: border-box; margin: 0; padding: 0; }
  html, body { width: 1200px; height: 1200px; overflow: hidden; background: var(--stage); }
  .flyer {
    position: absolute; left: 189px; top: 20px;
    width: 853px; height: 1204px;
    transform: scale(0.9635); transform-origin: 0 0;
    background: var(--ink); overflow: hidden;
    font-family: "Roboto", Arial, sans-serif; color: var(--paper);
  }
  .flyer > * { position: absolute; }
  .shapes { left: 0; top: 0; width: 853px; height: 1204px; }
  .photo {
    left: 370px; top: 20px; width: 483px; height: 725px;
    background: radial-gradient(ellipse 45% 55% at 58% 45%, #c98d6e 0%, #8a5a45 35%, #3a3a3f 65%, rgba(11,11,13,0) 100%);
  }
  .brand {
    left: 100px; top: 120px;
    display: flex; align-items: center; gap: 10px; white-space: nowrap;
    font-weight: 900; font-size: 24px; color: var(--ink); letter-spacing: 0.5px;
  }
  .brand-dot { width: 26px; height: 26px; border-radius: 50%; background: var(--pink); flex: none; }
  .title {
    left: 104px; top: 280px; width: 340px;
    font-family: "Teko", "Arial Narrow", sans-serif; font-weight: 500;
    font-size: 190px; line-height: 150px; color: var(--yellow); letter-spacing: 2px;
    transform: scaleX(0.72); transform-origin: 0 0;
  }
  .schedule {
    left: 58px; top: 567px; width: 328px; height: 201px;
    border: 1.5px solid var(--rule); padding: 12px 0 0 34px;
    font-weight: 700;
  }
  .schedule .date { font-size: 40px; line-height: 52px; }
  .schedule .days { font-size: 31px; line-height: 38px; }
  .schedule .hl { color: var(--yellow); }
  .schedule .date.hl { padding-left: 6px; }
  .schedule .days:first-of-type { margin-top: 4px; }
  .price-label { left: 186px; top: 786px; font-size: 28px; font-weight: 700; color: var(--sky); }
  .price-badge, .promo-badge {
    border-radius: 50%; background: linear-gradient(135deg, var(--pink), var(--purple) 50%, var(--blue));
    display: flex; align-items: center; justify-content: center;
  }
  .price-badge { left: 241px; top: 822px; width: 134px; height: 134px; }
  .price-badge .inner {
    width: 110px; height: 110px; border-radius: 50%; background: var(--paper);
    display: flex; align-items: center; justify-content: center;
    font-family: "Teko", sans-serif; font-weight: 500; font-size: 58px; color: var(--pink); padding-top: 8px;
  }
  .promo-badge { left: 30px; top: 943px; width: 212px; height: 212px; }
  .promo-badge .inner {
    width: 180px; height: 180px; border-radius: 50%; background: var(--paper);
    display: flex; flex-direction: column; align-items: center; justify-content: center;
    font-family: "Teko", sans-serif; color: var(--ink); text-align: center; line-height: 1;
  }
  .promo-badge .line { font-size: 22px; line-height: 25px; }
  .promo-badge .price { font-size: 36px; font-weight: 500; color: var(--pink); line-height: 34px; margin-top: 2px; }
  .promo-badge .tag { background: var(--ink); color: var(--paper); font-size: 19px; padding: 2px 5px 0; margin-top: 4px; }
  .venue {
    left: 453px; top: 788px; width: 356px; height: 93px; border: 1.5px solid #444;
    display: flex; align-items: center; justify-content: center;
    font-size: 34px; font-weight: 700; color: var(--yellow); padding-top: 12px;
  }
  .pin { left: 613px; top: 769px; width: 38px; height: 38px; }
  .welcome {
    right: 44px; top: 897px; font-size: 33px; font-weight: 700;
    padding-bottom: 6px; border-bottom: 2px solid var(--pink); width: 416px; text-align: right;
  }
  .join {
    right: 44px; top: 950px; font-family: "Teko", sans-serif; font-size: 37px;
    color: var(--sky); letter-spacing: 0.3px; white-space: nowrap;
  }
  .register {
    right: 44px; top: 996px; text-align: right;
    font-family: "Open Sans", Arial, sans-serif; font-size: 18px; line-height: 23px;
  }
  .register .hl { color: var(--yellow); }
  .terms {
    right: 44px; top: 1106px; text-align: right;
    font-family: "Open Sans", Arial, sans-serif; font-size: 14.5px; line-height: 19px; white-space: nowrap;
  }
</style>
</head>
<body>
<main class="flyer">
  <svg class="shapes" viewBox="0 0 853 1204" aria-hidden="true">
    <defs>
      <linearGradient id="stripe" x1="0" y1="1" x2="1" y2="0">
        <stop offset="0" stop-color="#e5168a"/>
        <stop offset="0.5" stop-color="#8a3fd1"/>
        <stop offset="1" stop-color="#1e9bdc"/>
      </linearGradient>
      <linearGradient id="stripe-rev" x1="0" y1="0" x2="1" y2="1">
        <stop offset="0" stop-color="#8a3fd1"/>
        <stop offset="1" stop-color="#e5168a"/>
      </linearGradient>
    </defs>
    <polygon points="0,0 508,0 300,246 96,246 0,345" fill="#ffffff"/>
    <polyline points="553,0 304,252 100,252 0,358" fill="none" stroke="url(#stripe)" stroke-width="8"/>
    <polygon points="500,0 553,0 464,90 446,110 446,80" fill="url(#stripe-rev)"/>
    <polygon points="0,330 68,260 68,296 0,370" fill="url(#stripe)"/>
    <polyline points="0,1204 448,746 710,746 853,560" fill="none" stroke="url(#stripe)" stroke-width="7"/>
    <polygon points="768,650 853,552 853,590 788,690" fill="url(#stripe)"/>
    <polygon points="0,1180 70,1108 110,1108 0,1204" fill="#1e9bdc"/>
    <polygon points="200,955 250,905 262,930 216,975" fill="#e5168a"/>
  </svg>

  <div class="photo" role="img" aria-label="Photo of a smiling woman in a grey sports top lifting a blue dumbbell"></div>

  <div class="brand"><span class="brand-dot"></span><span>LUMATREK GYM</span></div>

  <h1 class="title">BOOT CAMP</h1>

  <section class="schedule">
    <p class="date">22nd MARCH</p>
    <p class="date hl">- 26th APRIL</p>
    <p class="days">THURSDAYS 6pm</p>
    <p class="days hl">SATURDAYS 9am</p>
  </section>

  <p class="price-label">5 WEEKS</p>
  <div class="price-badge"><div class="inner">$100</div></div>

  <div class="promo-badge">
    <div class="inner">
      <span class="line">GET RESULTS</span>
      <span class="line">ALL YEAR ROUND!</span>
      <span class="price">ONLY $100</span>
      <span class="tag">5 WEEK BOOT CAMP</span>
    </div>
  </div>

  <div class="venue">BRINDMOOR GLEN</div>
  <svg class="pin" viewBox="0 0 38 38" aria-hidden="true">
    <circle cx="19" cy="19" r="18" fill="#0b0b0d" stroke="#555" stroke-width="1.5"/>
    <path d="M19 8c-4 0-7 3-7 7 0 5 7 13 7 13s7-8 7-13c0-4-3-7-7-7z" fill="#e5168a"/>
    <circle cx="19" cy="15" r="3" fill="#1e9bdc"/>
  </svg>

  <p class="welcome">ALL fitness levels welcome</p>
  <p class="join">JOIN IN ANY TIME! REGISTER YOUR PLACE NOW!</p>

  <div class="register">
    <p class="hl">Register now at</p>
    <p>lumatrekgym@mailvera.com</p>
    <p>or www.socialpage-example.com/lumatrekgymnz</p>
    <p class="hl">Female only. Registration essential.</p>
  </div>

  <div class="terms">
    <p>Valid from Mar 22, 2018 Expires 26th Apr, 2018</p>
    <p>Register online. Subject to availability. Valid for new clients only.</p>
    <p>Valid for unlimited sessions per week. Boot Camps run in 5 week blocks.</p>
    <p>Non-transferable. No refunds unless required by law. No cashback. Not to be used with any other offer.</p>
  </div>
</main>
</body>
</html>
```